Copper lark buildworks

Copper lark buildworks is a small construction company.
Who is a licenced builder, Carpenter, joiner,
working on heritage ,new build, speacial projects and sometimes furniture

Industry/Entity Type

Construction

```html
<!DOCTYPE html>
<html lang="en">
<head>
<meta charset="utf-8">
<title>Copper lark buildworks – Business Card</title>
<link rel="stylesheet" href="https://fonts.googleapis.com/css2?family=Open+Sans:wght@400;600;700&display=swap">
<style>
  :root {
    --backdrop: #a8a8a8;
    --card: #ffffff;
    --brand-green: #009440;
    --ink: #231f20;
    --on-green: #ffffff;
  }
  html, body {
    margin: 0;
    padding: 0;
    width: 1200px;
    height: 1000px;
    overflow: hidden;
    background: var(--backdrop);
    font-family: "Open Sans", Arial, sans-serif;
  }
  .canvas {
    position: relative;
    width: 1200px;
    height: 1000px;
  }
  .business-card {
    position: absolute;
    left: 171px;
    top: 247px;
    width: 795px;
    height: 494px;
    background: var(--card);
  }
  .holder-name {
    position: absolute;
    top: 52px;
    left: 0;
    width: 800px;
    text-align: center;
    margin: 0;
    font-size: 28px;
    font-weight: 400;
    color: var(--ink);
  }
  .brand-band {
    position: absolute;
    left: 14px;
    top: 214px;
    width: 767px;
    height: 177px;
    background: var(--brand-green);
    display: flex;
    align-items: center;
    justify-content: center;
  }
  .brand-name {
    margin: 0;
    font-size: 48px;
    font-weight: 600;
    color: var(--on-green);
    letter-spacing: 0.5px;
  }
  .phone-number {
    position: absolute;
    left: 214px;
    top: 420px;
    margin: 0;
    font-size: 30px;
    font-weight: 700;
    color: var(--ink);
    letter-spacing: 13px;
  }
</style>
</head>
<body>
  <main class="canvas">
    <section class="business-card">
      <p class="holder-name">Martin Hale</p>
      <div class="brand-band">
        <h1 class="brand-name">Copper lark buildworks</h1>
      </div>
      <p class="phone-number">0438276509</p>
    </section>
  </main>
</body>
</html>
```